Harlow Grading and Septic needs a flyer to submit to contractors to offer our services

I need a sleek profession one page full color high gloss document showcasing our services to give to Mobile Home Companies and contractors that need our services.

Home Builders. Mobile Home Salesmen. People Building new homes.

Construction

Serif
Sans Serif

• Phone Number. Email address. Logo. Services offered: Mobile Home Pads, Meter Pole Placement and Connection, Waterline Connection, On Site Septic System Installs
• Jokes, Nothing trying to be cute

```html
<!DOCTYPE html>
<html lang="en">
<head>
<meta charset="utf-8">
<title>Harlow Grading and Septic – Contractor Flyer</title>
<link href="https://fonts.googleapis.com/css2?family=Oswald:wght@400;500;600;700&family=Roboto+Condensed:ital,wght@1,300;1,400&display=swap" rel="stylesheet">
<style>
  :root {
    --page: #ffffff;
    --sheet: #ddebf7;
    --brand-blue: #0d4a87;
    --brand-red: #d0202a;
    --ink: #262626;
    --body-ink: #2b2b2b;
  }
  * { box-sizing: border-box; margin: 0; padding: 0; }
  html, body { width: 1200px; height: 1000px; overflow: hidden; background: var(--page); }
  .flyer {
    position: absolute; left: 341px; top: 133px;
    width: 518px; height: 733px;
    background: var(--sheet);
    font-family: "Oswald", sans-serif;
    overflow: hidden;
  }
  .flyer-phone {
    position: absolute; right: 31px; top: 27px;
    font-family: "Oswald", sans-serif; font-weight: 600; font-style: italic;
    font-size: 18px; color: var(--brand-red); letter-spacing: 0.2px;
  }
  .brand-name {
    position: absolute; left: 150px; top: 38px; width: 216px;
    text-align: center; color: var(--brand-blue);
    font-weight: 700; text-transform: uppercase; line-height: 1.05;
  }
  .brand-name .brand-main { display: block; font-size: 34px; letter-spacing: 2px; }
  .brand-name .brand-sub { display: block; font-size: 19px; letter-spacing: 0.6px; }
  .photo { position: absolute; }
  .photo-trench { left: 32px; top: 151px; width: 219px; height: 280px;
    background: linear-gradient(180deg, #5b7a3e 0%, #a9885a 30%, #b58552 65%, #9c6b3c 100%); }
  .photo-tank { left: 267px; top: 151px; width: 219px; height: 131px;
    background: linear-gradient(180deg, #2f63c4 0%, #6f97d8 55%, #c9c6bd 72%, #6f8d3e 100%); }
  .photo-install { left: 267px; top: 299px; width: 219px; height: 132px;
    background: linear-gradient(180deg, #5d8ac9 0%, #6a8a4a 25%, #cfa978 55%, #d8c4a3 100%); }
  .headline {
    position: absolute; left: 31px; top: 448px;
    font-weight: 700; font-size: 43px; line-height: 51px;
    color: var(--ink); letter-spacing: -0.5px;
    white-space: nowrap;
    transform: scaleX(0.84); transform-origin: left top;
  }
  .headline .accent-blue { color: var(--brand-blue); }
  .headline .accent-red { color: var(--brand-red); }
  .region-tag {
    position: absolute; left: 31px; top: 612px; width: 219px; height: 30px;
    background: var(--brand-blue); color: #fff;
    font-size: 17px; font-weight: 400; line-height: 30px; text-align: center;
    white-space: nowrap;
  }
  .services { position: absolute; left: 267px; top: 450px; width: 240px; list-style: none; }
  .service { position: absolute; left: 0; width: 240px; }
  .service-title { font-size: 16px; font-weight: 400; color: var(--brand-blue); line-height: 20px; white-space: nowrap; }
  .service-text {
    font-family: "Roboto Condensed", sans-serif; font-style: italic; font-weight: 400;
    font-size: 10px; line-height: 12.5px; color: var(--body-ink); margin-top: 2px;
  }
  .contact {
    position: absolute; left: 0; top: 668px; width: 100%;
    font-family: "Roboto Condensed", sans-serif; font-style: italic; font-weight: 300;
    font-size: 11.5px; color: var(--body-ink); text-align: center; line-height: 18px;
  }
  .contact-line { display: flex; justify-content: center; align-items: center; gap: 5px; }
  .contact-line svg { width: 10px; height: 10px; fill: var(--brand-blue); }
</style>
</head>
<body>
  <main class="flyer">
    <div class="flyer-phone">(903) 555-0148</div>

    <div class="brand-name">
      <span class="brand-main">Harlow</span>
      <span class="brand-sub">Grading and Septic</span>
    </div>

    <div class="photo photo-trench" role="img" aria-label="Excavator beside a mobile home with a worker in a freshly dug septic trench"></div>
    <div class="photo photo-tank" role="img" aria-label="Concrete septic tank being lowered from a boom truck in an open field"></div>
    <div class="photo photo-install" role="img" aria-label="Compact excavator next to an installed septic tank with green access lids"></div>

    <h1 class="headline">
      <span class="accent-blue">Expert</span> Mobile<br>
      Home Services<br>
      You Can <span class="accent-red">Trust</span>
    </h1>

    <div class="region-tag">Excavating Services in East Texas</div>

    <ul class="services">
      <li class="service" style="top:0">
        <h2 class="service-title">Mobile Home Pads</h2>
        <p class="service-text">Durable and stable pad installations for mobile homes.</p>
      </li>
      <li class="service" style="top:48px">
        <h2 class="service-title">Meter Pole Placement and Connection</h2>
        <p class="service-text">Professional meter pole placement and reliable<br>electrical connections.</p>
      </li>
      <li class="service" style="top:109px">
        <h2 class="service-title">Waterline Connection</h2>
        <p class="service-text">Efficient and secure waterline connections for new homes.</p>
      </li>
      <li class="service" style="top:157px">
        <h2 class="service-title">On Site Septic System Installs</h2>
        <p class="service-text">Comprehensive septic system installations for your property.</p>
      </li>
    </ul>

    <div class="contact">
      <div class="contact-line">
        <svg viewBox="0 0 10 10" aria-hidden="true"><path d="M0 2h10v6H0z"/><path d="M0.6 2.4L5 5.4l4.4-3" fill="none" stroke="#ddebf7" stroke-width="0.8"/></svg>
        <span>dale@harlowgradingandseptic.com</span>
      </div>
      <div class="contact-line">
        <svg viewBox="0 0 10 10" aria-hidden="true"><circle cx="5" cy="5" r="4.6"/><path d="M1 5h8M5 0.6c-2 2.5-2 6.3 0 8.8M5 0.6c2 2.5 2 6.3 0 8.8" fill="none" stroke="#ddebf7" stroke-width="0.7"/></svg>
        <span>harlowgradingandseptic.com</span>
      </div>
    </div>
  </main>
</body>
</html>
```